GPS business card

Brannery Works is the name of my company
GPS thats made to fit!

My Business is supply and install of IN DASH GPS SYSTEMS.
Small family based business that is mobile.

GPS touch screens that are built into the dash.
I have a logo I want Utilized
Wanting colours too

I have screens for all makes and models of vehicles.

I have attached a current business card and some photo's of the work I do.

Target Market(s)

new and used car buyers

Industry/Entity Type

Business

Requirements
Must have
• Name: Tom Brannery

Mob: 0438 215 604
email: tombrannery@mailvista.com

Must use logo

```html
<!DOCTYPE html>
<html lang="en">
<head>
<meta charset="utf-8">
<title>Brannery Works – Business Card</title>
<link rel="stylesheet" href="https://fonts.googleapis.com/css2?family=Della+Respira&display=swap">
<style>
  :root {
    --page-bg: #f8f8f8;
    --card-black: #000000;
    --gloss-mid: #2a2a2a;
    --gloss-light: #8a8a8a;
    --accent-orange: #f2a61c;
    --brand-blue: #1d7fd0;
    --text-white: #f4f4f4;
  }
  html, body {
    margin: 0;
    padding: 0;
    width: 1200px;
    height: 726px;
    overflow: hidden;
    background: var(--page-bg);
  }
  .canvas {
    position: relative;
    width: 1200px;
    height: 726px;
  }
  .card {
    position: absolute;
    left: 70px;
    top: 50px;
    width: 1055px;
    height: 605px;
    background:
      linear-gradient(129deg,
        var(--card-black) 42%,
        var(--gloss-mid) 60%,
        var(--gloss-light) 86%,
        var(--card-black) 86.6%);
    overflow: hidden;
    font-family: "Della Respira", serif;
    color: var(--text-white);
  }
  .accent-lines {
    position: absolute;
    left: 0;
    top: 0;
  }
  .brand {
    position: absolute;
    left: 0;
    right: 0;
    top: 88px;
    display: flex;
    justify-content: center;
    align-items: center;
    gap: 12px;
  }
  .brand-square {
    width: 40px;
    height: 40px;
    background: var(--brand-blue);
  }
  .brand-name {
    font-size: 30px;
    color: var(--accent-orange);
    white-space: nowrap;
  }
  .details {
    position: absolute;
    left: 121px;
    top: 170px;
  }
  .person-name {
    margin: 0;
    font-size: 64px;
    font-weight: normal;
    line-height: 1;
  }
  .person-role {
    margin: 4px 0 0;
    font-size: 44px;
    line-height: 1.1;
  }
  .contact {
    margin: 78px 0 0;
    font-size: 50px;
    line-height: 70px;
  }
  .contact span { display: block; }
</style>
</head>
<body>
<div class="canvas">
  <section class="card" aria-label="Brannery Works business card">
    <svg class="accent-lines" width="1055" height="605" viewBox="0 0 1055 605" aria-hidden="true">
      <path d="M85,120 Q88,103 105,103 L325,103" fill="none" stroke="var(--accent-orange)" stroke-width="6" stroke-linecap="round"/>
      <path d="M730,103 L950,103 Q967,103 970,120" fill="none" stroke="var(--accent-orange)" stroke-width="6" stroke-linecap="round"/>
    </svg>

    <div class="brand">
      <span class="brand-square" aria-hidden="true"></span>
      <span class="brand-name">Brannery Works</span>
    </div>

    <div class="details">
      <h1 class="person-name">Tom Brannery</h1>
      <p class="person-role">Installation Technician</p>
      <p class="contact">
        <span class="contact-phone">0438 - 215 - 604</span>
        <span class="contact-email">tombrannery@mailvista.com</span>
      </p>
    </div>
  </section>
</div>
</body>
</html>
```